Energy Drink label Velamo

Design a Label to be used on the packaging label/mock up for a energy drink. The name VELAMO means Black Bull & Bull ( in the 11 languages in the target country we want to launch ). I would like a in your face energy drink label design. Please see uploaded files as reference . Something out of the box thinking. For 500ml tin can label.

Target Market(s)

Population of Africa

Industry/Entity Type

Energy Drink

Colors
EB3D1F
EC4F4E
F09395
F8D3D4
FCEDEE

Requirements
Must have
• Bold and attractive design ( Black , Red , Silver , White ) as MAIN color scheme, as attached files I uploaded
Nice to have
• option of a white background and also black ( matte / carbon fibre effect )

```html
<!DOCTYPE html>
<html lang="en">
<head>
<meta charset="utf-8">
<title>Velamo Energy Drink Label</title>
<link rel="stylesheet" href="https://fonts.googleapis.com/css2?family=Anton&family=Bebas+Neue&display=swap">
<style>
  :root {
    --stage: #e9eaec;
    --label-black: #07070a;
    --label-charcoal: #1a1a1f;
    --glow-red: rgba(235, 61, 31, .38);
    --glow-red-soft: rgba(236, 79, 78, .22);
    --accent-red: #eb3d1f;
    --text-white: #ffffff;
    --silver: #b9bcc2;
    --silver-dark: #5d6066;
  }
  * { margin: 0; padding: 0; box-sizing: border-box; }
  html, body {
    width: 1200px; height: 771px; overflow: hidden;
    background: var(--stage);
  }
  .canvas { position: relative; width: 1200px; height: 771px; }
  .label {
    position: absolute; left: 400px; top: 35px;
    width: 401px; height: 700px; overflow: hidden;
    background:
      radial-gradient(ellipse 230px 150px at 300px 470px, var(--glow-red-soft), transparent 70%),
      radial-gradient(ellipse 190px 170px at 70px 120px, var(--glow-red), transparent 70%),
      radial-gradient(ellipse 260px 190px at 280px 650px, var(--glow-red), transparent 70%),
      linear-gradient(160deg, var(--label-black) 0%, var(--label-charcoal) 48%, var(--label-black) 100%);
    box-shadow: 6px 8px 14px rgba(0,0,0,.35);
  }
  .speed-band {
    position: absolute; width: 14px; height: 260px;
    background: linear-gradient(180deg, transparent, rgba(185,188,194,.35), transparent);
    transform: rotate(28deg);
  }
  .speed-band-top { left: 60px; top: -40px; }
  .speed-band-bottom { left: 320px; top: 470px; }
  .mascot-area {
    position: absolute; left: 62px; top: 38px; width: 262px; height: 250px;
    border-radius: 48% 52% 46% 46% / 44% 44% 56% 56%;
    background: radial-gradient(circle at 55% 45%, #3e3d42 0%, #1e1e22 58%, var(--silver-dark) 88%, var(--silver) 100%);
  }
  .brand-name {
    position: absolute; left: 0; top: 292px; width: 401px;
    font-family: "Anton", sans-serif; font-size: 92px; line-height: 1;
    color: var(--text-white); letter-spacing: 10px; text-indent: 10px; text-align: center;
  }
  .product-type {
    position: absolute; left: 31px; top: 404px;
    font-family: "Anton", sans-serif; font-size: 46px; line-height: 46px;
    letter-spacing: 2px;
    color: var(--accent-red); text-transform: uppercase;
  }
  .benefits {
    position: absolute; left: 208px; top: 406px; list-style: none;
    font-family: "Bebas Neue", sans-serif; font-size: 27px; line-height: 25px;
    letter-spacing: .5px;
    color: var(--text-white);
  }
  .benefits li { display: flex; align-items: center; gap: 6px; }
  .benefits svg { width: 15px; height: 15px; }
  .fact {
    position: absolute; text-align: center;
    font-family: "Bebas Neue", sans-serif; color: var(--text-white);
  }
  .fact .value { display: block; font-size: 38px; line-height: 32px; }
  .fact .unit { display: block; font-size: 19px; line-height: 18px; }
  .fact-calories { left: 46px; top: 530px; }
  .fact-caffeine { left: 124px; top: 528px; }
  .fact-volume { left: 74px; top: 604px; }
</style>
</head>
<body>
<div class="canvas">
  <section class="label">
    <div class="speed-band speed-band-top"></div>
    <div class="speed-band speed-band-bottom"></div>
    <div class="mascot-area" role="img" aria-label="Snarling black bull mascot with red eyes inside a silver shield"></div>
    <h1 class="brand-name">VELAMO</h1>
    <p class="product-type">Energy<br>Drink</p>
    <ul class="benefits">
      <li><svg viewBox="0 0 14 14"><path d="M1 7 L5 11 L13 2" fill="none" stroke="#fff" stroke-width="2.4"/></svg>Refuel</li>
      <li><svg viewBox="0 0 14 14"><path d="M1 7 L5 11 L13 2" fill="none" stroke="#fff" stroke-width="2.4"/></svg>Rehydrate</li>
      <li><svg viewBox="0 0 14 14"><path d="M1 7 L5 11 L13 2" fill="none" stroke="#fff" stroke-width="2.4"/></svg>Re-Energize</li>
    </ul>
    <div class="fact fact-calories"><span class="value">50</span><span class="unit">Calories</span></div>
    <div class="fact fact-caffeine"><span class="value">70 G</span><span class="unit">Caffeine</span></div>
    <div class="fact fact-volume"><span class="value">500 ML</span><span class="unit">Net Content</span></div>
  </section>
</div>
</body>
</html>
```